Quirky Label Design for an Exciting UK-Based Organic Skincare Company!

We need label designs across our range of products, we are a high quality yet quirky organic skincare company called Gently Velvety, we use frosted glass packaging, and we are just wanting one design done for now, but the winning designer we would want to work with to design the rest of the labels for us. We also want them to design business cards and other literature at some point and maybe even a website page.

Our label design will go on a 63mm tall frosted glass jar which is 62mm in diameter. The actual label dimensions should be, 170 mm (W) x 50 mm (H). The idea is so that it wraps around the whole jar with the design at one side (at the front) and the ingredients on another (at the back).

LABEL 1
Organic Polynesian Whipped Body Butter
Vanilla Bean
120ml

Made with Organic Shea and Cocoa Butters and exotic Monoi de Tahiti

Ingredients (INCI): Organic Raw Shea Butter (Butyrospermum Parkii), Organic Raw Cocoa Butter (Theobroma Cacao), Monoi de Tahiti (Coconut (Cocos nucifera) oil (and) Tiare (Gardenia tahitensis) flower), Organic Sweet Almond Oil (Prunus Amygdalus Dulcis), Organic Madagascan Vanilla Extract (Vanillin)

Handmade by Gently Velvety Ltd
14 Larkwell Lane, Bournemouth BH3 9QT, UK
Batch:

OPTIONAL WRITING (if it fits in):
100% Natural and Organic
Intensely Moisturising

LABEL 2
Mango Smoothie
120ml

Ingredients (INCI): Organic Raw Shea Butter (Butyrospermum Parkii), Organic Raw Cocoa Butter (Theobroma Cacao), Monoi de Tahiti (Coconut (Cocos nucifera) oil (and) Tiare (Gardenia tahitensis) flower), Organic Sweet Almond Oil (Prunus Amygdalus Dulcis), Organic Mango Flavour (Aroma)

Batch:

100% Natural and Organic
Intensely Moisturising

I have attached a picture of the jar we use and the lid we use for these products, as well as our logo. I've also attached a 'Handmade in Dorset' stamp which we'd like to go on there if possible, along with a shelf life symbol.

I am thinking the background colour of the labels will be either white or even brown paper colour. Perhaps it would be interesting to see it in both. UPDATE: We have decided on white background now, not brown.

The final design should denote handmade, organic, high quality, pure, yet quirky and original / unique. I am thinking perhaps a seemingly hand-drawn black leaf outline? Could fit the bill, but as I say, up to you. Something that says handmade yet professional.

I'd like to have the original Photoshop files from the winning designer so we can use them as a template for the rest of our horizontal labels.
Updates

Project Deadline Extended
Reason: Just need a few more days for designs we like to be worked on further, and to review new designs!

Target Market(s)

Everyone that appreciates a good quality skincare product focusing on natural & organic. Price is mid-range to high

Industry/Entity Type

It Company

Requirements
Must have
• Must make the product look high quality & organic yet quirky and accessible. Must have our logo and the shelf life symbol and the writing as above.
Nice to have
• Nice to have the 'handmade' stamp attached, but not absolutely necessary if it doesn't fit within your design.

```html
<!DOCTYPE html>
<html lang="en">
<head>
<meta charset="utf-8">
<title>Gently Velvety – Whipped Body Butter Labels</title>
<link rel="stylesheet" href="https://fonts.googleapis.com/css2?family=Lato:wght@300;400;700&family=Dancing+Script:wght@700&display=swap">
<style>
  :root {
    --canvas: #ffffff;
    --label-edge: #c9c9c9;
    --ink: #6d6e71;
    --ink-dark: #58595b;
    --leaf: #6ab650;
    --mango: #f6bf1a;
    --vanilla: #f2a188;
  }
  * { margin: 0; padding: 0; box-sizing: border-box; }
  html, body { width: 1200px; height: 1200px; overflow: hidden; background: var(--canvas); }
  body { position: relative; font-family: "Lato", sans-serif; color: var(--ink); }

  .label {
    position: absolute; left: 254px; width: 548px; height: 162px;
    border: 1px solid var(--label-edge); background: #fff;
  }
  .label--mango { top: 400px; --accent: var(--mango); }
  .label--vanilla { top: 630px; --accent: var(--vanilla); }

  .ingredients {
    position: absolute; left: 8px; top: 9px; width: 160px;
    font-size: 7.2px; line-height: 9.3px; font-weight: 300; text-align: justify;
  }
  .ingredients strong { font-weight: 700; }
  .maker {
    position: absolute; left: 8px; top: 104px; width: 170px;
    font-size: 7.2px; line-height: 9.3px; font-weight: 300;
  }

  .vine {
    position: absolute; left: 193px; top: 8px; width: 14px; height: 148px;
    background: linear-gradient(180deg, var(--leaf), #7cc462);
    opacity: .85; border-radius: 4px;
  }

  .front {
    position: absolute; left: 214px; top: 0; width: 120px; height: 162px; text-align: center;
  }
  .brand {
    position: absolute; left: 0; right: 0; top: 20px;
    display: flex; align-items: center; justify-content: center; gap: 5px;
    color: var(--leaf); font-size: 14px; font-weight: 700; line-height: 1.1;
  }
  .brand-dot { width: 8px; height: 8px; border-radius: 50%; background: var(--leaf); flex: none; }
  .product { position: absolute; left: -20px; right: -20px; top: 68px; font-weight: 300; color: var(--ink-dark); }
  .product-line1 { font-size: 14px; line-height: 16px; }
  .product-line2 { font-size: 11px; line-height: 14px; }
  .product-line3 {
    display: inline-block; font-size: 13px; line-height: 17px; margin-top: 4px;
    border-bottom: 1px solid var(--ink); padding: 0 2px 1px;
  }
  .flavour {
    position: absolute; left: -20px; right: -20px; top: 121px;
    font-family: "Dancing Script", cursive; font-size: 15px; color: var(--accent);
  }
  .volume { position: absolute; left: 0; right: 0; top: 142px; font-size: 13px; font-weight: 300; color: var(--ink-dark); }

  .stamp { position: absolute; left: 346px; top: 109px; width: 56px; height: 56px; }

  .claims { position: absolute; left: 423px; top: 48px; width: 120px; }
  .claims-figure { font-size: 20px; font-weight: 700; color: var(--ink); line-height: 22px; }
  .claims-text { font-size: 10px; font-weight: 300; line-height: 12.5px; }
  .made-with {
    margin-top: 15px; font-family: "Dancing Script", cursive; font-size: 10.5px; color: var(--ink-dark);
  }
  .made-with-list { font-size: 8.6px; font-weight: 300; line-height: 10.6px; }
</style>
</head>
<body>

<section class="label label--mango">
  <p class="ingredients"><strong>Ingredients (INCI):</strong> Organic Raw Shea Butter (Butyrospermum Parkii), Organic Raw Cocoa Butter (Theobroma Cacao), Monoi de Tahiti (Coconut (Cocos nucifera) oil (and) Tiare (Gardenia tahitensis) flower), Organic Sweet Almond Oil (Prunus Amygdalus Dulcis), Organic Madagascan Vanilla Extract (Vanillin).</p>
  <p class="maker">Handmade<br>by Gently Velvety Ltd<br>14 Larkwell Lane,<br>Bournemouth BH3 9QT, UK<br>Batch:</p>
  <div class="vine" role="img" aria-label="Vertical climbing leaf vine decoration"></div>
  <div class="front">
    <div class="brand"><span class="brand-dot"></span><span>Gently<br>Velvety</span></div>
    <div class="product">
      <div class="product-line1">ORGANIC</div>
      <div class="product-line2">POLYNESIAN WHIPPED</div>
      <div class="product-line3">BODY BUTTER</div>
    </div>
    <div class="flavour">mango smoothie</div>
    <div class="volume">120ml</div>
  </div>
  <svg class="stamp" viewBox="0 0 56 56" role="img" aria-label="Handmade stamp">
    <circle cx="28" cy="28" r="25" fill="none" stroke="var(--mango)" stroke-width="3"/>
  </svg>
  <div class="claims">
    <div class="claims-figure">100%</div>
    <div class="claims-text">Natural and Organic<br>Intensely Moisturising</div>
    <div class="made-with">made with</div>
    <div class="made-with-list">Organic Shea<br>&amp; Cocoa Butters<br>&amp; exotic Monoi de Tahiti</div>
  </div>
</section>

<section class="label label--vanilla">
  <p class="ingredients"><strong>Ingredients (INCI):</strong> Organic Raw Shea Butter (Butyrospermum Parkii), Organic Raw Cocoa Butter (Theobroma Cacao), Monoi de Tahiti (Coconut (Cocos nucifera) oil (and) Tiare (Gardenia tahitensis) flower), Organic Sweet Almond Oil (Prunus Amygdalus Dulcis), Organic Madagascan Vanilla Extract (Vanillin).</p>
  <p class="maker">Handmade<br>by Gently Velvety Ltd<br>14 Larkwell Lane,<br>Bournemouth BH3 9QT, UK<br>Batch:</p>
  <div class="vine" role="img" aria-label="Vertical climbing leaf vine decoration"></div>
  <div class="front">
    <div class="brand"><span class="brand-dot"></span><span>Gently<br>Velvety</span></div>
    <div class="product">
      <div class="product-line1">ORGANIC</div>
      <div class="product-line2">POLYNESIAN WHIPPED</div>
      <div class="product-line3">BODY BUTTER</div>
    </div>
    <div class="flavour">vanilla bean</div>
    <div class="volume">120ml</div>
  </div>
  <svg class="stamp" viewBox="0 0 56 56" role="img" aria-label="Handmade stamp">
    <circle cx="28" cy="28" r="25" fill="none" stroke="var(--vanilla)" stroke-width="3"/>
  </svg>
  <div class="claims">
    <div class="claims-figure">100%</div>
    <div class="claims-text">Natural and Organic<br>Intensely Moisturising</div>
    <div class="made-with">made with</div>
    <div class="made-with-list">Organic Shea<br>&amp; Cocoa Butters<br>&amp; exotic Monoi de Tahiti</div>
  </div>
</section>

</body>
</html>
```